LED Digital Boards - Directional Signs for Show Venue

We have 5 LED signs - Specs are attached
We have a show venue where we want to let our guests know where they are going. 5 simple designs required:
Photos: https://www.filebarn.example/sh/9k2m4p7q8r3s5t6/ZZqw_Lm3NbVx8Rt5Yh2KpWcDe?dl=0
1. FLOCK IN
PINK ARROWS Pointing Right
use Dapper album and use a feather girl
2. The Velvet Heron Mirrortent Carpark
(arrows pointing right)
Box Office
(arrows pointing left)
Another showgirl
3. Gold Member Ticket Holders Entry
(use a photo of cast member from TORQUE
4. Platinum Member Ticket Holders
(Use photo from Le Frisson - no nudity)
5. Welcome to Box Office
Collect and Book Tickets here
Pink feather girl
Very clean, simple, gold writing is always great and on brand for us.
Use fonts similar to Dapper Poster where is says VEGAS CABARET SHOW up the top. Can be similar, doesn't need to be exact.

```html
<!DOCTYPE html>
<html lang="en">
<head>
<meta charset="utf-8">
<title>Velvet Heron – Directional LED Boards</title>
<link rel="stylesheet" href="https://fonts.googleapis.com/css2?family=Montserrat:wght@700;800;900&display=swap">
<style>
  :root {
    --page: #ffffff;
    --purple-deep: #3a0a4a;
    --purple: #6a1a78;
    --purple-light: #9a2ca0;
    --pink: #ff2fa8;
    --pink-soft: #ff7fd0;
    --gold-light: #f6dd8a;
    --gold: #d8b04a;
    --gold-dark: #a57a22;
    --white: #ffffff;
    --ink: #2a0830;
  }
  * { box-sizing: border-box; margin: 0; padding: 0; }
  html, body { width: 1200px; height: 2804px; overflow: hidden; background: var(--page); }
  body { position: relative; font-family: "Montserrat", sans-serif; }

  .board {
    position: absolute; left: 140px; width: 920px; height: 456px; overflow: hidden;
    background: radial-gradient(ellipse at 50% 40%, var(--purple-light) 0%, var(--purple) 45%, var(--purple-deep) 100%);
    box-shadow: 0 10px 22px rgba(0,0,0,.35);
  }
  .board--flock { top: 148px; }
  .board--gold { top: 648px; }
  .board--platinum { top: 1152px; }
  .board--direction { top: 1652px; }
  .board--welcome { top: 2160px; }

  .light-swoosh { position: absolute; inset: 0; width: 100%; height: 100%; pointer-events: none; }

  .photo { position: absolute; }
  .photo--showgirl-left { left: 0; top: 0; width: 300px; height: 456px;
    background: linear-gradient(160deg, #f3b4cf 0%, #c85a9a 45%, #5a1860 100%); }
  .photo--host { right: 30px; top: 20px; width: 250px; height: 436px;
    background: linear-gradient(170deg, #6a4a3a 0%, #2a7a8a 40%, #1a3050 100%); }
  .photo--cast-group { left: 310px; top: 300px; width: 300px; height: 156px;
    background: linear-gradient(180deg, #8a5a6a 0%, #5a2a4a 100%); opacity: .9; }
  .photo--dancer { right: 0; top: 0; width: 380px; height: 456px;
    background: linear-gradient(150deg, #4a1850 0%, #c47090 45%, #7a3a5a 75%, #3a0a4a 100%); }
  .photo--singer { left: 40px; top: 250px; width: 330px; height: 206px;
    background: linear-gradient(140deg, #7a3a8a 0%, #d06090 50%, #4a1a5a 100%); }
  .photo--showgirl-right { right: 0; top: 0; width: 250px; height: 456px;
    background: linear-gradient(160deg, #f6c0d8 0%, #e070b0 45%, #6a1a70 100%); }

  .headline {
    position: absolute; font-weight: 900; text-transform: uppercase; line-height: .92; white-space: nowrap;
    background: linear-gradient(180deg, var(--gold-light) 0%, var(--gold) 55%, var(--gold-dark) 100%);
    -webkit-background-clip: text; background-clip: text; color: transparent;
  }
  .subline { position: absolute; font-weight: 800; color: var(--white); text-transform: uppercase; white-space: nowrap; }

  .brand {
    position: absolute; display: flex; align-items: center; gap: 8px; white-space: nowrap;
    font-weight: 900; color: var(--pink); font-size: 22px; text-transform: uppercase; letter-spacing: 1px;
  }
  .brand__dot { width: 20px; height: 20px; border-radius: 50%; background: var(--pink); }

  .arrow { position: absolute; width: 110px; height: 130px; }

  .ticket-bar {
    position: absolute; left: 300px; top: 364px; width: 350px; height: 44px;
    background: linear-gradient(180deg, var(--gold-light), var(--gold));
    color: var(--ink); font-weight: 800; font-size: 17px; white-space: nowrap;
    display: flex; align-items: center; justify-content: center; letter-spacing: .5px;
  }
</style>
</head>
<body>

<svg width="0" height="0" style="position:absolute">
  <defs>
    <linearGradient id="swooshPink" x1="0" x2="1">
      <stop offset="0" stop-color="#ff7fd0" stop-opacity="0"/>
      <stop offset=".5" stop-color="#ffb0e6" stop-opacity=".9"/>
      <stop offset="1" stop-color="#ff7fd0" stop-opacity="0"/>
    </linearGradient>
    <linearGradient id="arrowPink" x1="0" x2="1">
      <stop offset="0" stop-color="#ff5fc0"/>
      <stop offset="1" stop-color="#d21a8a"/>
    </linearGradient>
  </defs>
</svg>

<section class="board board--flock">
  <svg class="light-swoosh" viewBox="0 0 920 456" preserveAspectRatio="none">
    <path d="M0 380 C250 300 600 460 920 340" fill="none" stroke="url(#swooshPink)" stroke-width="4"/>
    <path d="M0 410 C300 340 620 480 920 380" fill="none" stroke="url(#swooshPink)" stroke-width="2"/>
  </svg>
  <div class="photo photo--showgirl-left" role="img" aria-label="Showgirl in pink feathered costume holding a feather fan"></div>
  <h1 class="headline" style="left:440px; top:80px; font-size:96px;">Flock<br>In</h1>
  <svg class="arrow" style="left:790px; top:95px;" viewBox="0 0 130 150" preserveAspectRatio="none">
    <rect x="4" y="4" width="122" height="142" fill="none" stroke="#ff5fc0" stroke-width="4"/>
    <path d="M30 20 L112 75 L30 130 Z" fill="url(#arrowPink)"/>
  </svg>
  <div class="brand" style="left:640px; top:320px;"><span class="brand__dot"></span>Velvet Heron</div>
</section>

<section class="board board--gold">
  <svg class="light-swoosh" viewBox="0 0 920 456" preserveAspectRatio="none">
    <path d="M0 60 C300 0 600 120 920 40" fill="none" stroke="url(#swooshPink)" stroke-width="3"/>
    <path d="M500 400 C650 300 820 360 920 300" fill="none" stroke="url(#swooshPink)" stroke-width="4"/>
  </svg>
  <div class="photo photo--cast-group" role="img" aria-label="Male cast members posing in a line"></div>
  <div class="photo photo--host" role="img" aria-label="Host in a sequinned jacket gesturing to the crowd"></div>
  <h2 class="headline" style="left:40px; top:50px; font-size:84px;">Gold<br>Member</h2>
  <p class="subline" style="left:42px; top:218px; font-size:32px;">Ticket Holders Entry</p>
  <div class="brand" style="left:40px; top:340px;"><span class="brand__dot"></span>Velvet Heron</div>
</section>

<section class="board board--platinum">
  <svg class="light-swoosh" viewBox="0 0 920 456" preserveAspectRatio="none">
    <path d="M0 330 C260 260 520 420 920 300" fill="none" stroke="url(#swooshPink)" stroke-width="4"/>
  </svg>
  <div class="photo photo--dancer" role="img" aria-label="Dancer in a pink sequinned costume striking a pose"></div>
  <h2 class="headline" style="left:40px; top:60px; font-size:76px;">Platinum<br>Member</h2>
  <p class="subline" style="left:42px; top:210px; font-size:34px;">Ticket Holders</p>
  <div class="brand" style="left:40px; top:340px;"><span class="brand__dot"></span>Velvet Heron</div>
</section>

<section class="board board--direction">
  <svg class="light-swoosh" viewBox="0 0 920 456" preserveAspectRatio="none">
    <path d="M0 240 C300 180 600 300 920 220" fill="none" stroke="url(#swooshPink)" stroke-width="3"/>
    <path d="M200 420 C450 360 700 440 920 400" fill="none" stroke="url(#swooshPink)" stroke-width="4"/>
  </svg>
  <svg class="arrow" style="left:30px; top:35px;" viewBox="0 0 130 150" preserveAspectRatio="none">
    <rect x="4" y="4" width="122" height="142" fill="none" stroke="#ff5fc0" stroke-width="4"/>
    <path d="M100 20 L18 75 L100 130 Z" fill="url(#arrowPink)"/>
  </svg>
  <h2 class="headline" style="left:170px; top:40px; font-size:78px;">Box<br>Office</h2>
  <div class="brand" style="left:650px; top:70px;"><span class="brand__dot"></span>Velvet Heron</div>
  <div class="photo photo--singer" role="img" aria-label="Performer singing on stage under pink lights"></div>
  <h2 class="headline" style="right:150px; top:250px; font-size:78px; text-align:right;">Car<br>Park</h2>
  <svg class="arrow" style="left:780px; top:270px;" viewBox="0 0 130 150" preserveAspectRatio="none">
    <rect x="4" y="4" width="122" height="142" fill="none" stroke="#ff5fc0" stroke-width="4"/>
    <path d="M30 20 L112 75 L30 130 Z" fill="url(#arrowPink)"/>
  </svg>
</section>

<section class="board board--welcome">
  <svg class="light-swoosh" viewBox="0 0 920 456" preserveAspectRatio="none">
    <path d="M0 40 C300 -10 600 110 920 30" fill="none" stroke="url(#swooshPink)" stroke-width="3"/>
  </svg>
  <div class="photo photo--showgirl-right" role="img" aria-label="Showgirl with a pink feather fan and feathered headdress"></div>
  <p class="subline" style="left:40px; top:120px; font-size:48px;">Welcome to</p>
  <h2 class="headline" style="left:40px; top:185px; font-size:88px;">Box Office</h2>
  <div class="brand" style="left:40px; top:375px;"><span class="brand__dot"></span>Velvet Heron</div>
  <div class="ticket-bar">COLLECT &amp; BOOK TICKETS HERE</div>
</section>

</body>
</html>
```